DL size flyer for Autism Consultancy website

We need a printed flyer DL size ( 210mmx99mm) for our Autism Consultancy website www.brightpathkids.nz which provides therapy for autistic children.
I want the flyer to look consistent with the website’s design. Please feel free to use the colour scheme, fonts, icons or any images from www.brightpathkids.nz.It should be easy to see “Autism” or “Autistic” word from a distance.
Please use either an oversized logo or make “Do you have a verbal and able autistic child?” more prominent.
Please do not convert the text fields to outlines, i.e. I need to be able to edit any text after.The final design should be either in Adobe Illustrator or Adobe Photoshop format.
The Specs for the flyer are
Document Trim Size99 x 210 mm 1169 x 2480 pixels
Full Bleed Size102 x 213 mm 1205 x 2516 pixels
Our Logo https://1drv.ms/u/s!AoH0rRjDY2GYg6QtU-xjoVlmslKp6gPlease
use this photo for the front side https://qzdropbin.io/f/Pw4KcN8rTyH2mXs6BvLd9QeFz1Gj
another one for reverse
https://qzdropbin.io/f/Rk2HsV5nWqJ7tZc3MfXb8LpYd4Ne
Please use the following content:
Do you have a verbal and able autistic child?
We use child-centred, modern and innovative approaches
Teaching autistic children to bond, laugh and play.
We work with schools
We help autistic children to develop social minds
We offer:
• Specialist assessments
• Consultations for parents & schools
• Social learning programmes
• Social-cognitive therapy
We can create an individual learning path, best suited for your child.
Our programmes and interventions include:
• Chatter Quest
• Peer Bright
• Team Puzzles
• Tingle Words
• Pebble Tales
• Pembrook Speech Ladder
• Vorlin Method
• BRIMLE Method
• Tandem Pattern Coaching
contact details on both sides:
www.brightpathkids.nz
info@brightpathkids.nz
(09) 57-318-46

```html
<!DOCTYPE html>
<html lang="en">
<head>
<meta charset="utf-8">
<title>Bright Path Kids – DL Flyer</title>
<link href="https://fonts.googleapis.com/css2?family=Germania+One&family=Roboto+Condensed:wght@400;500;700&family=Montserrat:wght@500;600;700&display=swap" rel="stylesheet">
<style>
  :root{
    --navy:#1b2a5a;
    --yellow:#f0c420;
    --teal:#3cbfb2;
    --white:#ffffff;
    --stage:#eceef1;
    --muted:#8f98b3;
  }
  *{box-sizing:border-box;margin:0;padding:0}
  html,body{width:1200px;height:1200px;overflow:hidden}
  body{background:var(--stage);position:relative;font-family:"Montserrat",sans-serif}
  .flyer{position:absolute;top:175px;width:400px;height:849px;background:var(--white);overflow:hidden;box-shadow:0 6px 18px rgba(0,0,0,.12)}
  .flyer--front{left:160px}
  .flyer--back{left:640px}
  .photo{position:absolute;left:0;top:0;width:400px}
  .flyer--front .photo{top:121px;height:380px;background:linear-gradient(160deg,#f4f2ef 0%,#e7dccf 40%,#c98a5a 70%,#e9d9c2 100%)}
  .flyer--back .photo{height:370px;background:linear-gradient(135deg,#d9b68e 0%,#e8cba8 40%,#d6453f 70%,#3a8fcf 100%)}
  .shapes{position:absolute;left:0;top:0;width:400px;height:849px}
  .txt{position:absolute;left:0;width:100%;text-align:center}

  .brand{position:absolute;display:flex;align-items:center;gap:10px}
  .brand__dot{border-radius:50%;background:var(--yellow);flex:none}
  .brand__name{font-family:"Montserrat",sans-serif;font-weight:700;color:var(--navy);line-height:1;white-space:nowrap}
  .flyer--front .brand{left:0;width:100%;justify-content:center;top:42px}
  .flyer--front .brand__dot{width:44px;height:44px}
  .flyer--front .brand__name{font-size:27px}
  .flyer--back .brand{left:196px;top:700px}
  .flyer--back .brand__dot{width:24px;height:24px}
  .flyer--back .brand__name{font-size:15px}

  .headline{font-family:"Germania One",sans-serif;font-weight:400;color:var(--navy);font-size:31px;line-height:37px;top:470px;letter-spacing:1px}
  .lead{font-family:"Roboto Condensed",sans-serif;font-weight:500;color:#111;font-size:23px;line-height:29px}
  .lead--approach{top:560px}
  .lead--play{top:629px}
  .lead--schools{top:693px;font-size:33px;line-height:38px}
  .tagline{font-family:"Roboto Condensed",sans-serif;font-weight:500;color:var(--muted);font-size:15px;top:782px}
  .web{font-family:"Montserrat",sans-serif;color:var(--white);font-size:17px;font-weight:500;top:805px}

  .pill{position:absolute;left:0;height:26px;background:var(--yellow);border-radius:0 13px 13px 0;color:var(--navy);font-weight:700;font-size:16px;line-height:26px;padding-left:25px}
  .pill--offer{top:326px;width:132px}
  .pill--programmes{top:531px;width:215px}
  .list{position:absolute;list-style:none}
  .list li{display:flex;align-items:center;gap:9px;color:#2b2f3a;font-weight:500;white-space:nowrap}
  .tick{width:11px;height:11px;flex:none}
  .list--offer{left:26px;top:365px}
  .list--offer li{font-size:13.5px;height:25px}
  .list--prog li{font-size:12px;height:25px}
  .list--prog-a{left:26px;top:564px}
  .list--prog-b{left:167px;top:564px}
  .statement{position:absolute;left:24px;top:474px;color:var(--navy);font-weight:700;font-size:14px;line-height:18px}
  .phone{top:782px;color:var(--white);font-weight:700;font-size:18px;display:flex;justify-content:center;align-items:center;gap:6px}
  .contacts{top:808px;display:flex;justify-content:center;gap:18px;color:var(--white);font-size:12px;font-weight:500}
  .contacts span{display:flex;align-items:center;gap:6px}
  .icon{width:12px;height:12px;flex:none}
</style>
</head>
<body>

<section class="flyer flyer--front">
  <div class="brand">
    <span class="brand__dot"></span>
    <span class="brand__name">Bright Path Kids</span>
  </div>
  <div class="photo" role="img" aria-label="Photo of a therapist sitting with a smiling young boy holding a teddy bear in a bright playroom"></div>
  <svg class="shapes" viewBox="0 0 400 849" aria-hidden="true">
    <path d="M0 444 Q180 418 400 478" fill="none" stroke="var(--teal)" stroke-width="9"/>
    <path d="M0 450 Q180 424 400 484 L400 740 Q220 795 0 706 Z" fill="var(--yellow)"/>
    <path d="M0 712 Q220 801 400 746" fill="none" stroke="var(--teal)" stroke-width="9"/>
    <path d="M0 718 Q220 807 400 752 L400 849 L0 849 Z" fill="var(--navy)"/>
  </svg>
  <h1 class="txt headline">Do you have a verbal<br>and able autistic child?</h1>
  <p class="txt lead lead--approach">We use child-centred, modern<br>and innovative approaches</p>
  <p class="txt lead lead--play">Teaching autistic children to<br>bond, laugh and play.</p>
  <p class="txt lead lead--schools">We work with schools</p>
  <p class="txt tagline">We help autistic children to develop social minds</p>
  <p class="txt web">www.brightpathkids.nz</p>
</section>

<section class="flyer flyer--back">
  <div class="photo" role="img" aria-label="Photo of a young boy in a striped shirt lying on the floor playing with toy cars"></div>
  <svg class="shapes" viewBox="0 0 400 849" aria-hidden="true">
    <path d="M0 296 Q230 276 400 355" fill="none" stroke="var(--teal)" stroke-width="9"/>
    <path d="M0 302 Q230 282 400 361 L400 849 L0 849 Z" fill="var(--white)"/>
    <path d="M0 706 Q200 790 400 742" fill="none" stroke="var(--teal)" stroke-width="9"/>
    <path d="M0 712 Q200 796 400 748 L400 849 L0 849 Z" fill="var(--navy)"/>
  </svg>

  <div class="pill pill--offer">WE OFFER</div>
  <ul class="list list--offer">
    <li><svg class="tick" viewBox="0 0 12 12"><circle cx="6" cy="6" r="6" fill="var(--navy)"/><path d="M3.3 6.2l1.8 1.8 3.6-3.7" fill="none" stroke="#fff" stroke-width="1.6"/></svg>Specialist assessments</li>
    <li><svg class="tick" viewBox="0 0 12 12"><circle cx="6" cy="6" r="6" fill="var(--navy)"/><path d="M3.3 6.2l1.8 1.8 3.6-3.7" fill="none" stroke="#fff" stroke-width="1.6"/></svg>Consultations for parents &amp; schools</li>
    <li><svg class="tick" viewBox="0 0 12 12"><circle cx="6" cy="6" r="6" fill="var(--navy)"/><path d="M3.3 6.2l1.8 1.8 3.6-3.7" fill="none" stroke="#fff" stroke-width="1.6"/></svg>Social learning programmes</li>
    <li><svg class="tick" viewBox="0 0 12 12"><circle cx="6" cy="6" r="6" fill="var(--navy)"/><path d="M3.3 6.2l1.8 1.8 3.6-3.7" fill="none" stroke="#fff" stroke-width="1.6"/></svg>Social-cognitive therapy</li>
  </ul>
  <p class="statement">We can create an individual learning path,<br>best suited for your child.</p>

  <div class="pill pill--programmes">OUR PROGRAMMES</div>
  <ul class="list list--prog list--prog-a">
    <li><svg class="tick" viewBox="0 0 12 12"><circle cx="6" cy="6" r="6" fill="var(--navy)"/><path d="M3.3 6.2l1.8 1.8 3.6-3.7" fill="none" stroke="#fff" stroke-width="1.6"/></svg>Chatter Quest</li>
    <li><svg class="tick" viewBox="0 0 12 12"><circle cx="6" cy="6" r="6" fill="var(--navy)"/><path d="M3.3 6.2l1.8 1.8 3.6-3.7" fill="none" stroke="#fff" stroke-width="1.6"/></svg>Peer Bright</li>
    <li><svg class="tick" viewBox="0 0 12 12"><circle cx="6" cy="6" r="6" fill="var(--navy)"/><path d="M3.3 6.2l1.8 1.8 3.6-3.7" fill="none" stroke="#fff" stroke-width="1.6"/></svg>Team Puzzles</li>
    <li><svg class="tick" viewBox="0 0 12 12"><circle cx="6" cy="6" r="6" fill="var(--navy)"/><path d="M3.3 6.2l1.8 1.8 3.6-3.7" fill="none" stroke="#fff" stroke-width="1.6"/></svg>Tingle Words</li>
    <li><svg class="tick" viewBox="0 0 12 12"><circle cx="6" cy="6" r="6" fill="var(--navy)"/><path d="M3.3 6.2l1.8 1.8 3.6-3.7" fill="none" stroke="#fff" stroke-width="1.6"/></svg>Pebble Tales</li>
  </ul>
  <ul class="list list--prog list--prog-b">
    <li><svg class="tick" viewBox="0 0 12 12"><circle cx="6" cy="6" r="6" fill="var(--navy)"/><path d="M3.3 6.2l1.8 1.8 3.6-3.7" fill="none" stroke="#fff" stroke-width="1.6"/></svg>Pembrook Speech Ladder</li>
    <li><svg class="tick" viewBox="0 0 12 12"><circle cx="6" cy="6" r="6" fill="var(--navy)"/><path d="M3.3 6.2l1.8 1.8 3.6-3.7" fill="none" stroke="#fff" stroke-width="1.6"/></svg>Vorlin Method</li>
    <li><svg class="tick" viewBox="0 0 12 12"><circle cx="6" cy="6" r="6" fill="var(--navy)"/><path d="M3.3 6.2l1.8 1.8 3.6-3.7" fill="none" stroke="#fff" stroke-width="1.6"/></svg>BRIMLE Method</li>
    <li><svg class="tick" viewBox="0 0 12 12"><circle cx="6" cy="6" r="6" fill="var(--navy)"/><path d="M3.3 6.2l1.8 1.8 3.6-3.7" fill="none" stroke="#fff" stroke-width="1.6"/></svg>Tandem Pattern Coaching</li>
  </ul>

  <div class="brand">
    <span class="brand__dot"></span>
    <span class="brand__name">Bright Path Kids</span>
  </div>

  <p class="txt phone">
    <svg class="icon" viewBox="0 0 24 24" style="width:16px;height:16px"><path d="M6.6 10.8a15 15 0 006.6 6.6l2.2-2.2c.3-.3.7-.4 1-.2 1.1.4 2.3.6 3.6.6.6 0 1 .4 1 1V20c0 .6-.4 1-1 1A17 17 0 013 4c0-.6.4-1 1-1h3.5c.6 0 1 .4 1 1 0 1.3.2 2.5.6 3.6.1.3 0 .7-.2 1z" fill="var(--teal)"/></svg>
    (09) 57-318-46
  </p>
  <div class="txt contacts">
    <span><svg class="icon" viewBox="0 0 24 24"><rect x="2" y="5" width="20" height="14" rx="2" fill="none" stroke="var(--teal)" stroke-width="2.2"/><path d="M3 6l9 7 9-7" fill="none" stroke="var(--teal)" stroke-width="2.2"/></svg>info@brightpathkids.nz</span>
    <span><svg class="icon" viewBox="0 0 24 24"><circle cx="12" cy="12" r="9.5" fill="none" stroke="var(--teal)" stroke-width="2.2"/><ellipse cx="12" cy="12" rx="4" ry="9.5" fill="none" stroke="var(--teal)" stroke-width="2"/><path d="M2.5 12h19" stroke="var(--teal)" stroke-width="2"/></svg>www.brightpathkids.nz</span>
  </div>
</section>

</body>
</html>
```